Financial Coaching & Personal Development

I’m desiring a classic business card for my financial coaching and personal development business. The colors I have started with are a goldish brown and hunter green. The brownish color represents soil and green represents growth. I don’t want it it to look masculine. I want the brown to be more of a golden color. I want the color combination and overall design to be timeless not trendy. The logo can be changed as long as it represents growth- moving from where you are to where you want to be.

Target Market(s)

Working Adults with median income $65k; small businesses with a minimum of 20 employees

Industry/Entity Type

Consulting

Contact Information for Business Card

Marla Pettit, MBA
Certified Financial Coach

Font styles to use
Serif

Requirements
Must have
• Logo
My name
Business description
Email marla.pettit@brightwaycoachhub
Phone number 555-314-7829
Nice to have
• Slogan

```html
<!DOCTYPE html>
<html lang="en">
<head>
<meta charset="utf-8">
<title>Brightway Coach Hub – Business Cards</title>
<link href="https://fonts.googleapis.com/css2?family=Philosopher:wght@400;700&display=swap" rel="stylesheet">
<style>
  :root {
    --gold-brown: #7a5c12;
    --hunter-green: #2a8c0a;
    --card-white: #ffffff;
    --backdrop: #e6e1db;
    --band-line: #6b4a12;
  }
  * { box-sizing: border-box; margin: 0; padding: 0; }
  html, body { width: 1200px; height: 1200px; overflow: hidden; }
  body {
    background: var(--backdrop);
    font-family: "Philosopher", Georgia, serif;
    position: relative;
  }
  .card {
    position: absolute;
    top: 435px;
    width: 540px;
    height: 330px;
    background: var(--card-white);
    box-shadow: 0 6px 14px rgba(0,0,0,0.12);
    overflow: hidden;
  }
  .card--front { left: 40px; }
  .card--back { left: 620px; }

  .brand-dot {
    position: absolute;
    left: 50%;
    transform: translateX(-50%);
    border-radius: 50%;
    background: var(--hunter-green);
  }
  .card--front .brand-dot { top: 66px; width: 92px; height: 92px; }
  .card--back .brand-dot { top: 42px; width: 86px; height: 86px; }

  .brand-name {
    position: absolute;
    left: 0; right: 0;
    text-align: center;
    color: var(--gold-brown);
    font-weight: 700;
    text-transform: uppercase;
    letter-spacing: 1.5px;
  }
  .card--front .brand-name { top: 196px; font-size: 24px; }
  .card--back .brand-name { top: 170px; font-size: 23px; }

  .tagline {
    position: absolute;
    left: 0; right: 0;
    text-align: center;
    color: var(--hunter-green);
    font-size: 16px;
  }
  .card--front .tagline { top: 226px; }
  .card--back .tagline { top: 198px; }

  .person-name {
    position: absolute;
    top: 220px; left: 0; right: 0;
    text-align: center;
    color: var(--gold-brown);
    font-size: 22px;
  }
  .person-title {
    position: absolute;
    top: 246px; left: 0; right: 0;
    text-align: center;
    color: var(--hunter-green);
    font-size: 23px;
    font-weight: 700;
  }

  .footer-band {
    position: absolute;
    left: 0; right: 0; bottom: 0;
    height: 49px;
    background: var(--hunter-green);
    border-top: 3px solid var(--band-line);
  }
  .contact {
    position: absolute;
    left: 38px; top: 8px;
    color: #ffffff;
    font-size: 12.5px;
    line-height: 15px;
  }
</style>
</head>
<body>
  <section class="card card--front">
    <div class="brand-dot"></div>
    <div class="brand-name">Brightway Coach Hub</div>
    <div class="tagline">Financial Education &amp; Personal Development</div>
    <div class="footer-band"></div>
  </section>

  <section class="card card--back">
    <div class="brand-dot"></div>
    <div class="brand-name">Brightway Coach Hub</div>
    <div class="tagline">Financial Education &amp; Personal Development</div>
    <div class="person-name">Marla Pettit, MBA</div>
    <div class="person-title">Certified Financial Coach</div>
    <div class="footer-band">
      <div class="contact">
        <div>Email marla.pettit@brightwaycoachhub</div>
        <div>Phone number 555-314-7829</div>
      </div>
    </div>
  </section>
</body>
</html>
```